Visitenkarten-Design für App Start Up
Zielgruppe
Wir sind ein Start-Up und haben unsere Kotremo App gerelauncht.
Wir haben zwei Zielgruppen für unsere App. Zum einen lokale Gewerbetreibende, welche in Echtzeit Angebote (Coupons) erstellen können und zum anderen private User, welche diese innerhalb eines vorgegebenen Zeitraumes reservieren und einlösen können.
Hierfür müssen wir auch unsere Visitenkarten auf unser neues Design anpassen.
Aufgabenstellung
Visitenkarten sollten beidseitig bedruckt sein und auf der Vorderseite sollte unser Kotremo Logo und/oder der App Name Kotremo versehen sein. Auf der Rückseite benötigen wir die Infos: Name, Position, Firma inkl. Anschrift, E-Mail sowie die Telefonnummer.
Ansonsten freuen wir uns auf weitere kreative Ansätze.

```html
<!DOCTYPE html>
<html lang="de">
<head>
<meta charset="utf-8">
<title>Kotremo Visitenkarte</title>
<link rel="stylesheet" href="https://fonts.googleapis.com/css2?family=Montserrat:wght@500&family=Poppins:wght@400;600&display=swap">
<style>
  :root {
    --backdrop: #1eae99;
    --card: #ffffff;
    --ink: #2b2d30;
    --ink-soft: #45474b;
    --magenta: #c63a85;
    --violet: #7a5fa0;
    --blue: #0896d0;
    --icon: #3a78b8;
  }
  * { box-sizing: border-box; margin: 0; padding: 0; }
  html, body { width: 1200px; height: 849px; overflow: hidden; }
  body { background: var(--backdrop); position: relative; font-family: "Poppins", sans-serif; color: var(--ink); }

  .card {
    position: absolute;
    width: 439px;
    height: 282px;
    background: var(--card);
    overflow: hidden;
  }
  .card--front { left: 118px; top: 279px; }
  .card--back { left: 612px; top: 278px; }

  .card__band {
    position: absolute;
    left: 0; right: 0; bottom: 0;
    height: 9px;
    background: linear-gradient(90deg, var(--magenta), var(--violet) 50%, var(--blue));
  }

  /* Front */
  .brand-mark {
    position: absolute;
    left: 50%;
    top: 100px;
    width: 34px;
    height: 34px;
    margin-left: -17px;
    background: var(--magenta);
  }
  .brand-name {
    position: absolute;
    left: 0; right: 0;
    top: 182px;
    text-align: center;
    font-family: "Montserrat", sans-serif;
    font-weight: 500;
    font-size: 32px;
    letter-spacing: 3px;
    line-height: 1;
    color: var(--ink);
  }

  /* Back */
  .person { position: absolute; left: 60px; top: 108px; }
  .person__name { font-weight: 600; font-size: 16.5px; line-height: 1.1; color: var(--ink); }
  .person__role { font-size: 12px; line-height: 1.2; color: var(--ink-soft); }

  .contact { position: absolute; left: 60px; top: 170px; list-style: none; }
  .contact__item {
    display: flex; align-items: center;
    height: 20.5px;
    font-size: 11.5px;
    color: var(--ink-soft);
  }
  .contact__icon { width: 12px; height: 12px; margin-right: 10px; flex: none; }

  .back-brand {
    position: absolute;
    left: 269px; top: 92px;
    display: flex; align-items: center; gap: 8px;
  }
  .back-brand__mark { width: 18px; height: 18px; background: var(--magenta); }
  .back-brand__name {
    font-family: "Poppins", sans-serif;
    font-weight: 600;
    font-size: 20px;
    letter-spacing: 1px;
    color: var(--ink);
  }

  .company { position: absolute; left: 269px; top: 188px; font-size: 11px; line-height: 13px; color: var(--ink-soft); font-style: normal; }
  .company__name { font-weight: 600; color: var(--ink); }
</style>
</head>
<body>

  <section class="card card--front" aria-label="Vorderseite">
    <span class="brand-mark"></span>
    <p class="brand-name">KOTREMO</p>
    <span class="card__band"></span>
  </section>

  <section class="card card--back" aria-label="Rückseite">
    <div class="person">
      <p class="person__name">Jan Probemeyer</p>
      <p class="person__role">Geschäftsführer</p>
    </div>

    <ul class="contact">
      <li class="contact__item">
        <svg class="contact__icon" viewBox="0 0 24 24" fill="none" stroke="var(--icon)" stroke-width="2.2" stroke-linejoin="round"><path d="M5 3h4l2 5-2.5 1.5a11 11 0 0 0 6 6L16 13l5 2v4a2 2 0 0 1-2 2A17 17 0 0 1 3 5a2 2 0 0 1 2-2z"/></svg>
        04711/ 362514
      </li>
      <li class="contact__item">
        <svg class="contact__icon" viewBox="0 0 24 24" fill="none" stroke="var(--icon)" stroke-width="2.2" stroke-linejoin="round"><rect x="2" y="5" width="20" height="14"/><path d="M7 10l5 4 5-4"/></svg>
        mail@kotremo.de
      </li>
      <li class="contact__item">
        <svg class="contact__icon" viewBox="0 0 24 24" fill="none" stroke="var(--icon)" stroke-width="2"><circle cx="12" cy="12" r="10"/><ellipse cx="12" cy="12" rx="4.5" ry="10"/><path d="M2 12h20"/></svg>
        www.kotremo.de/info
      </li>
    </ul>

    <div class="back-brand">
      <span class="back-brand__mark"></span>
      <span class="back-brand__name">KOTREMO</span>
    </div>

    <address class="company">
      <span class="company__name">KOTREMO GmbH</span><br>
      Lindenweg 7<br>
      54321 Beispielfeld
    </address>

    <span class="card__band"></span>
  </section>

</body>
</html>
```